Business Intelligence/Analytics Technology Company Business Card

We are a higher-end enterprise software development company working with Retailer POS data to provide business intelligence and analytical services to fortune 500 companies.

I have an immediate need for a professional/thick/bold business card. The same design aspects will spiral into more media such as flyers/folders/etc...

Our website is www.kovenmrx.com for our product.

I like "Clean" designs if that makes sense, not a lot of "stuff".

The uploaded files, the A logo with the box is the style we're leaning towards, but the A logo without the blue box is all good too... get creative.

Target Market(s)

Executives of large companies, down to VP level..

Industry/Entity Type

Software

Requirements
Must have
• I'm wanting a thick designer like business card.

I think we're going to change our logo to a more lumora 6 looking style... http://www.kovenmrx.com/card.ai as an example of our current business card.

The winner will also have knowledge of where i can get these things printed.
Nice to have
• Blue-ish color scheme? I'm open to anything. Our Competition is Red, and another is Green. So we'll stick with the Blue.

```html
<!DOCTYPE html>
<html lang="en">
<head>
<meta charset="utf-8">
<title>KOVEN Business Card</title>
<link rel="stylesheet" href="https://fonts.googleapis.com/css2?family=Source+Sans+3:wght@400;600&display=swap">
<style>
  :root {
    --stage: #2e2e30;
    --brand-blue: #0a69c6;
    --brand-blue-light: #1a78d2;
    --ink: #2a2a2a;
    --card-white: #ffffff;
    --card-grey: #dcdddf;
  }
  * { margin: 0; padding: 0; box-sizing: border-box; }
  html, body { width: 1200px; height: 900px; overflow: hidden; }
  body {
    background: var(--stage);
    font-family: "Source Sans 3", "Myriad Pro", Arial, sans-serif;
    position: relative;
  }
  .card {
    position: absolute;
    top: 308px;
    width: 513px;
    height: 283px;
    border-radius: 20px;
    overflow: hidden;
  }
  /* Front */
  .card-front {
    left: 73px;
    background: linear-gradient(160deg, var(--brand-blue) 0%, var(--brand-blue-light) 55%, var(--brand-blue) 100%);
    color: var(--card-white);
  }
  .front-mark {
    position: absolute;
    left: 106px;
    top: 108px;
    width: 60px;
    height: 66px;
    background: var(--card-white);
  }
  .front-name {
    position: absolute;
    left: 193px;
    top: 118px;
    font-size: 40px;
    font-weight: 400;
    letter-spacing: 26px;
    line-height: 1;
    color: var(--card-white);
  }
  .front-url {
    position: absolute;
    left: 0;
    right: 0;
    top: 236px;
    text-align: center;
    font-size: 14px;
    color: var(--card-white);
  }
  /* Back */
  .card-back {
    left: 616px;
    background: linear-gradient(150deg, var(--card-grey) 0%, #f1f1f2 45%, var(--card-white) 65%, #ededee 100%);
    color: var(--ink);
  }
  .back-mark {
    position: absolute;
    left: 103px;
    top: 92px;
    width: 58px;
    height: 64px;
    background: var(--brand-blue);
  }
  .back-name {
    position: absolute;
    left: 42px;
    top: 165px;
    font-size: 30px;
    font-weight: 400;
    letter-spacing: 17px;
    line-height: 1;
    color: var(--brand-blue);
  }
  .divider {
    position: absolute;
    left: 257px;
    top: 39px;
    width: 2px;
    height: 206px;
    background: var(--brand-blue);
  }
  .details {
    position: absolute;
    right: 27px;
    top: 36px;
    text-align: right;
    font-size: 12.5px;
    line-height: 15px;
  }
  .person-name {
    font-size: 17px;
    font-weight: 600;
    line-height: 21px;
    color: var(--brand-blue);
  }
  .person-title {
    font-size: 17px;
    line-height: 20px;
    margin-bottom: 10px;
  }
  .company {
    font-weight: 600;
    color: var(--brand-blue);
    font-size: 12px;
  }
  .group { margin-bottom: 16px; }
  .group.personal { margin-bottom: 26px; }
  .line { display: flex; justify-content: flex-end; align-items: center; gap: 4px; }
  .personal .line { font-size: 14px; line-height: 17px; }
  .icon { width: 10px; height: 10px; flex: none; fill: var(--brand-blue); }
</style>
</head>
<body>

<section class="card card-front" aria-label="Card front">
  <div class="front-mark"></div>
  <div class="front-name">KOVEN</div>
  <div class="front-url">www.kovenmrx.com</div>
</section>

<section class="card card-back" aria-label="Card back">
  <div class="back-mark"></div>
  <div class="back-name">KOVEN</div>
  <div class="divider"></div>

  <div class="details">
    <div class="person-name">Damian Holloway</div>
    <div class="person-title">President</div>

    <div class="group personal">
      <div class="line">555 014 2231
        <svg class="icon" viewBox="0 0 10 10"><path d="M2.5 0h5v10h-5zM3.5 1v7h3V1z"/></svg>
      </div>
      <div class="line">damian@kovenmrx.com
        <svg class="icon" viewBox="0 0 10 10"><path d="M0 2h10v6H0zM0.8 2.6 5 5.6 9.2 2.6z" fill-rule="evenodd"/></svg>
      </div>
    </div>

    <div class="group">
      <div class="line company">KOVEN Technology Group, Inc</div>
      <div class="line">48 Linden Avenue
        <svg class="icon" viewBox="0 0 10 10"><path d="M5 0a3.5 3.5 0 0 1 3.5 3.5C8.5 6 5 10 5 10S1.5 6 1.5 3.5A3.5 3.5 0 0 1 5 0zm0 2a1.5 1.5 0 1 0 0 3 1.5 1.5 0 0 0 0-3z" fill-rule="evenodd"/></svg>
      </div>
      <div class="line">Millbrook, New York 12545</div>
    </div>

    <div class="group">
      <div class="line">555 016 4870
        <svg class="icon" viewBox="0 0 10 10"><circle cx="5" cy="5" r="5"/><path d="M3.2 2.5l1 1-.6.8c.4.8 1.1 1.5 1.9 1.9l.8-.6 1 1-.8.9C4.9 7.3 2.7 5.1 2.5 3.3z" fill="#fff"/></svg>
      </div>
      <div class="line">555 019 3362
        <svg class="icon" viewBox="0 0 10 10"><path d="M2.5 0h5v3h-5zM0 3.5h10v4H8V6H2v1.5H0zM2.5 6.5h5V10h-5z"/></svg>
      </div>
      <div class="line">www.kovenmrx.com
        <svg class="icon" viewBox="0 0 10 10"><circle cx="5" cy="5" r="4.4" fill="none" stroke="#0a69c6" stroke-width="1.1"/><ellipse cx="5" cy="5" rx="1.9" ry="4.4" fill="none" stroke="#0a69c6" stroke-width="0.9"/><path d="M0.6 5h8.8M1.3 2.8h7.4M1.3 7.2h7.4" stroke="#0a69c6" stroke-width="0.8"/></svg>
      </div>
    </div>
  </div>
</section>

</body>
</html>
```